Business cards and stationery for medical company
Business cards, letter heads & envelopes
Professional
Dr.Felix Barsow
President and CEO
418 Tallowfield Lane
Ashgrove, OH 43519 USA
fbarsow@curavista.us
www.curavista.us
Please use the 1-st option color on white background.

```html
<!DOCTYPE html>
<html lang="en">
<head>
<meta charset="utf-8">
<title>CuraVista business cards</title>
<link rel="stylesheet" href="https://fonts.googleapis.com/css2?family=Arimo:wght@400;700&display=swap">
<style>
  :root {
    --backdrop: #ecebe8;
    --card: #ffffff;
    --brand-blue: #1f5fa8;
    --brand-red: #c8282d;
    --text-grey: #4a4a4a;
    --rule: #c9ccd2;
    --shadow: rgba(0, 0, 0, 0.18);
  }
  * { box-sizing: border-box; margin: 0; padding: 0; }
  html, body { width: 1200px; height: 773px; overflow: hidden; }
  body {
    background: var(--backdrop);
    font-family: "Arimo", Arial, sans-serif;
    position: relative;
  }
  .card {
    position: absolute;
    width: 520px;
    height: 300px;
    background: var(--card);
    border-radius: 22px;
    box-shadow: 0 6px 18px var(--shadow);
  }
  .card-front { left: 50px; top: 236px; }
  .card-back  { left: 630px; top: 236px; }

  .brand-lockup {
    position: absolute;
    left: 40px; top: 58px;
    display: flex; align-items: center; gap: 12px;
  }
  .brand-dot {
    width: 34px; height: 34px; border-radius: 50%;
    background: var(--brand-red);
  }
  .brand-name {
    font-weight: 700; font-size: 34px; color: var(--brand-blue);
    letter-spacing: -0.5px;
  }
  .person { position: absolute; left: 40px; top: 140px; }
  .person-name { color: var(--brand-blue); font-size: 19px; font-weight: 700; }
  .person-title { color: var(--brand-red); font-size: 14px; margin-top: 2px; }
  .address {
    position: absolute; left: 40px; top: 200px;
    color: var(--text-grey); font-size: 13px; line-height: 1.45;
  }
  .divider {
    position: absolute; left: 275px; top: 128px;
    width: 1px; height: 132px; background: var(--rule);
  }
  .contact-list {
    position: absolute; left: 292px; top: 132px;
    list-style: none; color: var(--text-grey); font-size: 13px;
  }
  .contact-list li {
    display: flex; align-items: center; gap: 9px; height: 30px;
  }
  .contact-icon { width: 16px; height: 16px; flex: none; }

  .back-name {
    position: absolute; left: 0; right: 0; top: 112px;
    text-align: center; font-weight: 700; font-size: 52px;
    color: var(--brand-blue); letter-spacing: -0.5px;
  }
  .back-url {
    position: absolute; left: 0; right: 0; top: 218px;
    text-align: center; font-size: 15px; letter-spacing: 4px;
    color: var(--text-grey);
  }
</style>
</head>
<body>
  <section class="card card-front">
    <div class="brand-lockup">
      <span class="brand-dot"></span>
      <span class="brand-name">CuraVista</span>
    </div>
    <div class="person">
      <p class="person-name">Dr.Felix Barsow</p>
      <p class="person-title">President and CEO</p>
    </div>
    <p class="address">418 Tallowfield Lane<br>Ashgrove, OH 43519 USA</p>
    <div class="divider"></div>
    <ul class="contact-list">
      <li>
        <svg class="contact-icon" viewBox="0 0 16 16"><circle cx="8" cy="8" r="8" fill="#1f5fa8"/><path d="M5 4.5c.6-.5 1.2-.2 1.5.4l.5 1c.2.4 0 .8-.3 1l-.4.3c.4.9 1.1 1.6 2 2l.3-.4c.2-.3.6-.5 1-.3l1 .5c.6.3.9.9.4 1.5-.7.8-1.8.9-3 .2C6.5 9.9 5.4 8.8 4.8 7.5c-.6-1.2-.5-2.3.2-3z" fill="#fff"/></svg>
        (555) 240-1186
      </li>
      <li>
        <svg class="contact-icon" viewBox="0 0 16 16"><circle cx="8" cy="8" r="8" fill="#1f5fa8"/><rect x="5.5" y="3.5" width="5" height="9" rx="1" fill="#fff"/><rect x="6.5" y="5" width="3" height="5" fill="#1f5fa8"/></svg>
        (555) 317-4420
      </li>
      <li>
        <svg class="contact-icon" viewBox="0 0 16 16"><circle cx="8" cy="8" r="8" fill="#1f5fa8"/><rect x="4" y="6.5" width="8" height="5" rx="1" fill="#fff"/><rect x="5.5" y="4" width="5" height="3" fill="#fff"/></svg>
        (555) 862-0375
      </li>
      <li>
        <svg class="contact-icon" viewBox="0 0 16 16"><circle cx="8" cy="8" r="8" fill="#1f5fa8"/><rect x="4" y="5" width="8" height="6" fill="#fff"/><path d="M4 5l4 3.5L12 5" stroke="#1f5fa8" stroke-width="1" fill="none"/></svg>
        fbarsow@curavista.us
      </li>
    </ul>
  </section>

  <section class="card card-back">
    <p class="back-name">CuraVista</p>
    <p class="back-url">www.curavista.us</p>
  </section>
</body>
</html>
```